Website for a start-up named Trx SolumWave.

The company is currently producing a sustainable tactical training measure for soldiers in the defense industry. We’d like a simple website design. As the product hasn’t been launched yet, we will not tell too much about the product and it’s not for sale either. We have a website on wix called trxsolumwave.com which we would like to proceed with. The design just needs a professional and loving touch. We develop an add on for KZ90 rifles.

Target Market(s)

Defense industry

Industry/Entity Type

Defense

Coding

Coded - Design and coding required

Number of Pages Required

1 page

```html
<!DOCTYPE html>
<html lang="en">
<head>
<meta charset="utf-8">
<title>Trx SolumWave</title>
<link href="https://fonts.googleapis.com/css2?family=Ubuntu:ital,wght@0,400;0,500;1,400;1,500&display=swap" rel="stylesheet">
<style>
:root{
  --teal:#00a69c;
  --ink:#2f2f2f;
  --dark-btn:#2b2b2b;
  --footer:#232323;
  --white:#ffffff;
}
*{margin:0;padding:0;box-sizing:border-box}
html,body{width:1200px;height:3722px;overflow:hidden}
body{position:relative;font-family:"Ubuntu",sans-serif;color:var(--ink);background:var(--white)}
a{text-decoration:none}
.abs{position:absolute}

/* header */
.site-header{left:0;top:0;width:1200px;height:118px;background:var(--white)}
.brand{left:172px;top:36px;font-size:30px;font-weight:500;color:var(--teal);letter-spacing:.5px}
.main-nav{left:519px;top:47px;display:flex;font-size:16px;text-transform:uppercase;color:#333}
.main-nav a{color:inherit;margin-right:29px}
.main-nav a:last-child{margin-right:0}

/* hero */
.hero{left:0;top:118px;width:1200px;height:633px;
  background:linear-gradient(180deg,#5d6a5e 0%,#7d8a72 35%,#6f8a52 70%,#6b7f4a 100%)}
.hero-photo{left:0;top:0;width:1200px;height:633px;
  background:radial-gradient(ellipse at 78% 45%,#3a4a3e 0%,rgba(60,70,60,.6) 25%,rgba(0,0,0,0) 55%)}
.hero-title{left:172px;top:315px;font-size:66px;font-weight:500;color:var(--white)}

/* intro */
.intro-title{left:172px;top:884px;font-size:38px;font-weight:500;color:#333}
.intro-title span{color:var(--teal)}
.intro-sub{left:172px;top:943px;font-size:18px;font-weight:500;color:#333}
.intro-text{left:172px;top:988px;width:438px;font-size:12.5px;line-height:31.5px;text-align:justify;color:#333}
.btn{display:block;font-size:17px;font-weight:500;text-transform:uppercase;color:var(--white);text-align:center;line-height:57px;height:57px}
.btn-teal{left:172px;top:1177px;width:124px;background:var(--teal)}
.btn-dark{background:var(--dark-btn)}
.intro-photo{left:660px;top:859px;width:540px;height:400px;
  background:linear-gradient(160deg,#545454 0%,#7a7a74 40%,#3d3d3d 100%)}

/* who we are */
.who{left:0;top:1346px;width:1200px;height:580px;background:var(--teal)}
.who-photo{left:0;top:0;width:604px;height:580px;
  background:linear-gradient(120deg,#5b6a56 0%,#8b9476 45%,#6f8db0 100%);
  clip-path:polygon(0 0,604px 0,495px 286px,604px 580px,0 580px)}
.section-heading{font-size:38px;font-weight:500;color:var(--white);text-transform:uppercase;line-height:54px}
.who-heading{left:621px;top:94px}
.section-text{font-size:12.5px;line-height:27px;color:var(--white);text-align:justify}
.who-text{left:621px;top:184px;width:407px}
.who-btn{left:621px;top:393px;width:124px}

/* technology */
.tech{left:0;top:1925px;width:1200px;height:580px;background:var(--teal)}
.tech-photo{left:595px;top:0;width:605px;height:580px;
  background:linear-gradient(110deg,#b9bcb3 0%,#d2d4cc 35%,#8f9478 70%,#5d6b48 100%);
  clip-path:polygon(9px 0,605px 0,605px 580px,0 580px,110px 289px)}
.tech-heading{left:174px;top:73px}
.tech-text{left:174px;top:191px;width:446px}
.tech-text p+p{margin-top:5px}
.tech-btn{left:174px;top:445px;width:124px}

/* testimonials */
.testimonials{left:0;top:2505px;width:1200px;height:621px;
  background:linear-gradient(120deg,#d9dcdd 0%,#eeefef 35%,#f1f1f1 65%,#e3e4e2 100%)}
.testi-heading{left:0;top:124px;width:1200px;text-align:center;font-size:38px;font-weight:500;color:#333}
.testi-heading span{color:var(--teal)}
.quote-open{left:188px;top:184px}
.quote-close{left:928px;top:390px}
.testi-title{left:0;top:200px;width:1200px;text-align:center;font-size:19px;font-style:italic;font-weight:500;color:#333}
.testi-text{left:190px;top:262px;width:826px;text-align:center;font-size:12px;font-style:italic;line-height:27px;color:#333}
.testi-author{left:0;top:432px;width:1200px;text-align:center;font-size:16px;font-weight:500;color:#333}

/* footer */
.footer{left:0;top:3126px;width:1200px;height:596px;background:var(--footer);color:var(--white)}
.footer-heading{left:172px;top:104px;font-size:38px;font-weight:500;text-transform:uppercase}
.contact-item{left:172px;display:flex;align-items:center;font-size:17px;text-transform:uppercase;letter-spacing:.4px}
.contact-item svg{margin-right:18px}
.map{left:524px;top:96px;width:504px;height:341px;background:linear-gradient(135deg,#4a4a4a,#3c3c3c 60%,#454545)}
.footer-rule{left:172px;top:504px;width:856px;height:2px;background:var(--white)}
.copyright{left:0;top:540px;width:1200px;text-align:center;font-size:16px}
</style>
</head>
<body>

<header class="site-header abs">
  <div class="brand abs">Trx SolumWave</div>
  <nav class="main-nav abs">
    <a href="#">Home</a><a href="#">About</a><a href="#">Our Technology</a><a href="#">Blog Post</a><a href="#">Contact</a>
  </nav>
</header>

<section class="hero abs">
  <div class="hero-photo abs" role="img" aria-label="Woman aiming a rifle at an outdoor shooting range"></div>
  <div class="hero-title abs">Trx SolumWave</div>
</section>

<section class="intro">
  <h1 class="intro-title abs">TRX <span>SOLUMWAVE</span></h1>
  <p class="intro-sub abs">Sustainable solutions to the defense industry</p>
  <p class="intro-text abs">Welcome to Trx SolumWave, the advanced Technology Company paving the way to the future. We are a team of like-minded and determined individuals, all sharing a vision for success. We believe that our sophisticated technology has the potential to become an industry sensation. Would you like to find out more? Our website will be updated on a regular basis.</p>
  <a class="btn btn-teal abs" href="#">Read More</a>
  <div class="intro-photo abs" role="img" aria-label="Two officers training at an indoor shooting range with paper targets"></div>
</section>

<section class="who abs">
  <div class="who-photo abs" role="img" aria-label="Shooter in a cap aiming a tactical rifle at a target"></div>
  <h2 class="section-heading who-heading abs">Who We Are</h2>
  <p class="section-text who-text abs">Trx SolumWave is a leading provider of cutting-edge technologies and services, offering scalable solutions for the defense and security industry of all sizes. Founded by a group of friends who started by scrib bling their ideas on a bus ride in San Francisco. Today we are working on innovative solutions to disrupt the training industry with a sustainable solution.</p>
  <a class="btn btn-dark who-btn abs" href="#">Read More</a>
</section>

<section class="tech abs">
  <div class="tech-photo abs" role="img" aria-label="Shooter with ear protection firing a pistol outdoors"></div>
  <h2 class="section-heading tech-heading abs">Our Innovative<br>Technology</h2>
  <div class="section-text tech-text abs">
    <p>At Trx SolumWave, our comprehensive technological solutions help the industry to become more sustainable and efficient with the spendings. We will balance qualitative training experience for soldiers and security forces with real life experiences and a real life feel.</p>
    <p>Our platform will have a wide range of features created with the aim to help the industry become more aware of their environmental footprint. In order to empower our users to do better, Trx SolumWave is continually building upon its technology.</p>
  </div>
  <a class="btn btn-dark tech-btn abs" href="#">Read More</a>
</section>

<section class="testimonials abs" role="img" aria-label="Faded background photo of a shooter in a cap">
  <h2 class="testi-heading abs">OUR <span>TESTIMONIALS</span></h2>
  <svg class="quote-open abs" width="80" height="62" viewBox="0 0 80 62" aria-hidden="true">
    <path fill="#00a69c" d="M4 62c-5-14-3-30 6-42C17 10 26 3 36 0l2 5c-9 5-15 12-16 22 8 1 14 7 14 15 0 11-8 20-19 20H4zm40 0c-5-14-3-30 6-42C57 10 66 3 76 0l2 5c-9 5-15 12-16 22 8 1 14 7 14 15 0 11-8 20-19 20H44z"/>
  </svg>
  <p class="testi-title abs">"The secret of getting ahead is getting started"</p>
  <p class="testi-text abs">"Nemo enim ipsam voluptatem quia voluptas sit aspernatur aut odit aut fugit, sed quia consequuntur magni dolores eos qui ratione volupta tem sequi nesciunt. Neque porro quisquam est, qui dolorem ipsum quia dolor sit amet, consectetur, adipisci velit, sed quia non numquam eius modi tempora incidunt ut labore et dolore magnam aliquam quaerat voluptatem. Ut enim ad minima veniam, quis nostrum exercitationem ullam corporis suscipit laboriosam, nisi ut aliquid ex ea commodi consequatur."</p>
  <p class="testi-author abs">- ELIAS MARLOWE</p>
  <svg class="quote-close abs" width="80" height="62" viewBox="0 0 80 62" aria-hidden="true">
    <path fill="#00a69c" d="M76 0c5 14 3 30-6 42-7 10-16 17-26 20l-2-5c9-5 15-12 16-22-8-1-14-7-14-15C44 9 52 0 63 0h13zM36 0c5 14 3 30-6 42-7 10-16 17-26 20l-2-5c9-5 15-12 16-22C10 34 4 28 4 20 4 9 12 0 23 0h13z"/>
  </svg>
</section>

<footer class="footer abs">
  <h2 class="footer-heading abs">Get In Touch</h2>
  <div class="contact-item abs" style="top:177px">
    <svg width="46" height="46" viewBox="0 0 46 46" aria-hidden="true"><circle cx="23" cy="23" r="23" fill="#00a69c"/><path d="M23 12c-5 0-8.5 3.7-8.5 8.3 0 6 8.5 13.7 8.5 13.7s8.5-7.7 8.5-13.7C31.5 15.7 28 12 23 12z" fill="none" stroke="#fff" stroke-width="1.8"/><circle cx="23" cy="20.5" r="3" fill="none" stroke="#fff" stroke-width="1.8"/></svg>
    <span>Norvik Strand 14, 2.</span>
  </div>
  <div class="contact-item abs" style="top:245px">
    <svg width="46" height="46" viewBox="0 0 46 46" aria-hidden="true"><circle cx="23" cy="23" r="23" fill="#00a69c"/><rect x="13" y="16" width="20" height="14" fill="none" stroke="#fff" stroke-width="1.8"/><path d="M13 16l10 8 10-8" fill="none" stroke="#fff" stroke-width="1.8"/></svg>
    <span>info@trxsolumwave.com</span>
  </div>
  <div class="contact-item abs" style="top:312px">
    <svg width="46" height="46" viewBox="0 0 46 46" aria-hidden="true"><circle cx="23" cy="23" r="23" fill="#00a69c"/><path d="M16 13l4 0 2 6-3 2c1.5 3 3.5 5 6 6l2-3 6 2v4c0 1-1 2-2 2-9-1-16-8-17-17 0-1 1-2 2-2z" fill="none" stroke="#fff" stroke-width="1.8" stroke-linejoin="round"/></svg>
    <span>+45 20481763</span>
  </div>
  <div class="map abs" role="img" aria-label="Street map showing the office location"></div>
  <div class="footer-rule abs"></div>
  <p class="copyright abs">Copyrights @ 2021 Trx SolumWave. All Rights Reserved.</p>
</footer>

</body>
</html>
```